Design Creative Banner or Gif Ads. 3 Designs To Be Selected

Come up with some creative banner ads for crestline.co.nz

*At least 3 different winning banners will be chosen*

Please provide banner ads / gif ads in common google ads / website banner formats.

They can be gif or static but must stand out while still maintaining clear clean text and visuals, with a premium professional feel (please avoid clip art or anything that gives a cheap message).

Please keep in mind that these will likely be small ads so text needs to be large and if there's there a lot of text then use multiple frames/ pages as submit as a gif.

Style
Minimal & clean lines
Architectural or realistic images
Avoid cartoon styles, clipart, or anything that looks cheap

Font
Nexa or Montserrat or similar

Tone
Premium, serious, trustworthy — fits new builds

Colours
Option 1: Deep Navy (trust & quality) & lighter blues and warm grey
Option 2: Open to bright colours to help the ads stand out, such as (but not limited to) bright pink with black, yellow, fluorescent green, provided the messaging is still done professionally.
Our logo is attached (Crest Line Logo)

Display Sizes
Ad specs for file sizes should be file formats like JPEG, GIF, and PNG, with animations limited to a max of 30 seconds or less.
We will need several different ad sizes provided for each of the 3 selected winning designs.

• Medium Rectangle: 300 × 250 pixels
• Leaderboard: 728 × 90 pixels
• Desktop Banner ad image: (640x360 pixels)
• Desktop Banner ad image 2: (300x600 pixels)
• Possibly one or two other sizes

Flexibility to be creative
The ad text, words, upper/lower case, layout, colour, theme, and images can be adjusted to how you think it will look best. The follow example ads are just examples of what we are after but we are keen to see what you can create.

Recommendations at this point:
1. Avoid text heavy
2. Looking for more Gif ads
3. Imaging: if possible use real stock photo's rather than AI

Themes:

1
Building Soon? Start Here
Free Build Planning Pack:
✓ Build Cost Calculator
✓ Hidden Cost Checklist
✓ Builder Comparison Guide
Build With Confidence
Download Free

2
Before You Choose A Builder
Compare Price, Scope, Risk & Value
Avoid Costly Mistakes
Choose The Right Builder With Confidence
Download The Free Guide

3
Planning A New Build?
Avoid These Common Mistakes:
✗ Hidden Exclusions
✗ Missing Scope
✗ Unrealistic Allowances
✗ Budget Blowouts
Download The Free Guide

4
Before You Buy Land
Know what it could cost to build.
Avoid Costly Building Mistakes
Download Our Free Guides

5
Know Your Build Budget?
• Free Build Cost Calculator
• Hidden Cost Checklist
• Build Planning Tools
Calculate Costs (Download)

Target Market(s)

Landowners looking to build

Industry/Entity Type

Building

Font styles to use
Other font styles liked:
• Nexa or Montserrat or similar

Requirements
Should not have
• Avoid cartoon styles, clipart, or anything that looks cheap

```html
<!DOCTYPE html>
<html lang="en">
<head>
<meta charset="utf-8">
<title>Crest Line – The Cheapest Quote Doesn't Show The Whole Picture</title>
<link rel="stylesheet" href="https://fonts.googleapis.com/css2?family=Montserrat:wght@500;600;700;800&display=swap">
<style>
  :root {
    --sky-top: #1a2d4d;
    --sky-horizon: #3e6790;
    --sea-surface: #1f5f94;
    --sea-mid: #123f6e;
    --sea-deep: #071a36;
    --white: #ffffff;
    --tagline: #b9d6f0;
  }
  * { margin: 0; padding: 0; box-sizing: border-box; }
  html, body {
    width: 800px;
    height: 1200px;
    overflow: hidden;
    background: var(--sea-deep);
  }
  .ad {
    position: relative;
    width: 800px;
    height: 1200px;
    overflow: hidden;
    font-family: "Montserrat", sans-serif;
    color: var(--white);
  }
  .backdrop {
    position: absolute;
    inset: 0;
    background: linear-gradient(to bottom,
      var(--sky-top) 0%,
      var(--sky-horizon) 30%,
      var(--sea-surface) 34%,
      var(--sea-mid) 62%,
      var(--sea-deep) 100%);
  }
  .brand {
    position: absolute;
    left: 30px;
    top: 30px;
    display: flex;
    align-items: center;
    gap: 50px;
  }
  .brand-mark {
    width: 100px;
    height: 100px;
    background: var(--white);
  }
  .brand-name {
    font-size: 56px;
    font-weight: 700;
    line-height: 1;
  }
  .brand-tagline {
    margin-top: 12px;
    font-size: 15px;
    font-weight: 600;
    letter-spacing: 0.3px;
    color: var(--tagline);
  }
  .headline {
    position: absolute;
    left: 24px;
    top: 207px;
    font-size: 72px;
    font-weight: 800;
    line-height: 86px;
    letter-spacing: -0.5px;
  }
  .subline {
    position: absolute;
    left: 30px;
    top: 839px;
    font-size: 39px;
    font-weight: 600;
    line-height: 50px;
  }
  .risks {
    position: absolute;
    left: 476px;
    top: 460px;
    list-style: none;
  }
  .risk {
    position: absolute;
    left: 0;
    display: flex;
    align-items: flex-start;
    white-space: nowrap;
    font-size: 33px;
    font-weight: 600;
    line-height: 40px;
  }
  .risk-pointer {
    flex: none;
    width: 74px;
    height: 40px;
    margin-right: 14px;
  }
</style>
</head>
<body>
  <main class="ad">
    <div class="backdrop" role="img" aria-label="Photograph of an iceberg in a dusky sea, its small tip above the waterline and a far larger mass hidden beneath the surface"></div>

    <header class="brand">
      <div class="brand-mark"></div>
      <div>
        <div class="brand-name">Crest Line</div>
        <div class="brand-tagline">COMPARE QUOTES FROM TRUSTED BUILDERS</div>
      </div>
    </header>

    <h1 class="headline">The<br>Cheapest<br>Quote<br>Doesn’t<br>Show The<br>Whole<br>Picture.</h1>

    <p class="subline">Spot missing<br>items that<br>could turn<br>into expensive<br>variations later</p>

    <ul class="risks">
      <li class="risk" style="top:0">
        <svg class="risk-pointer" viewBox="0 0 74 40"><circle cx="5" cy="20" r="4" fill="#fff"/><line x1="5" y1="20" x2="72" y2="20" stroke="#fff" stroke-width="2"/></svg>
        <span>Provisional<br>Sums</span>
      </li>
      <li class="risk" style="top:126px">
        <svg class="risk-pointer" viewBox="0 0 74 40"><circle cx="5" cy="20" r="4" fill="#fff"/><line x1="5" y1="20" x2="72" y2="20" stroke="#fff" stroke-width="2"/></svg>
        <span>Exclusions</span>
      </li>
      <li class="risk" style="top:216px">
        <svg class="risk-pointer" viewBox="0 0 74 40"><circle cx="5" cy="20" r="4" fill="#fff"/><line x1="5" y1="20" x2="72" y2="20" stroke="#fff" stroke-width="2"/></svg>
        <span>Variations</span>
      </li>
      <li class="risk" style="top:304px">
        <svg class="risk-pointer" viewBox="0 0 74 40"><circle cx="5" cy="20" r="4" fill="#fff"/><line x1="5" y1="20" x2="72" y2="20" stroke="#fff" stroke-width="2"/></svg>
        <span>Site Costs</span>
      </li>
      <li class="risk" style="top:392px">
        <svg class="risk-pointer" viewBox="0 0 74 40"><circle cx="5" cy="20" r="4" fill="#fff"/><line x1="5" y1="20" x2="72" y2="20" stroke="#fff" stroke-width="2"/></svg>
        <span>Delays</span>
      </li>
      <li class="risk" style="top:484px">
        <svg class="risk-pointer" viewBox="0 0 74 40"><circle cx="5" cy="20" r="4" fill="#fff"/><line x1="5" y1="20" x2="72" y2="20" stroke="#fff" stroke-width="2"/></svg>
        <span>Quality<br>Risks</span>
      </li>
    </ul>
  </main>
</body>
</html>
```